Brennick Holdings Business Cards

These are professional business cards that are for my family office.
Put fake emails and phone numbers as of now until I finalize those components. This family office controls my families investments, assets, and future. The cards should be professional.
..
.
.
.
I just uploaded another variation of a logo I would like to see as a business card to I am inbeteen which logo to use

Target Market(s)

business

Industry/Entity Type

business

Contact Information for Business Card

Professional, wealth related, finance related.

Requirements
Must have
• Logo

```html
<!DOCTYPE html>
<html lang="en">
<head>
<meta charset="UTF-8">
<title>Brennick Holdings Business Cards</title>
<link href="https://fonts.googleapis.com/css2?family=Cinzel:wght@400;600;700&display=swap" rel="stylesheet">
<style>
  :root {
    --backdrop: #3b3b3d;
    --card: #ffffff;
    --navy: #1b1f2d;
    --ink: #2a2d36;
    --faint: #ececec;
  }
  html, body {
    margin: 0;
    padding: 0;
    width: 1200px;
    height: 1059px;
    overflow: hidden;
    background: var(--backdrop);
  }
  .canvas {
    position: relative;
    width: 1200px;
    height: 1059px;
  }
  .card {
    position: absolute;
    background: var(--card);
    border-radius: 22px;
    overflow: hidden;
    font-family: "Cinzel", serif;
    color: var(--navy);
  }
  .card--front { left: 256px; top: 100px; width: 688px; height: 393px; }
  .card--back  { left: 253px; top: 536px; width: 694px; height: 396px; }

  .contact-column {
    position: absolute;
    left: 0;
    top: 0;
    width: 352px;
    text-align: center;
  }
  .company-heading {
    position: absolute;
    left: 0; width: 352px;
    top: 26px;
    margin: 0;
    font-size: 31px;
    font-weight: 600;
    letter-spacing: 0.5px;
    white-space: nowrap;
  }
  .person-name {
    position: absolute;
    left: 0; width: 352px;
    top: 88px;
    margin: 0;
    font-size: 33px;
    font-weight: 600;
    letter-spacing: 1px;
  }
  .person-title {
    position: absolute;
    left: 0; width: 352px;
    top: 134px;
    margin: 0;
    font-size: 17px;
    font-weight: 400;
    letter-spacing: 1px;
    color: var(--ink);
  }
  .icon-row {
    position: absolute;
    left: 0; width: 352px;
    top: 175px;
    height: 28px;
  }
  .rule {
    position: absolute;
    height: 2px;
    background: var(--navy);
  }
  .rule--left  { left: 60px;  top: 189px; width: 63px; }
  .rule--right { left: 228px; top: 189px; width: 63px; }
  .rule--divider { left: 73px; top: 306px; width: 206px; }
  .icon {
    position: absolute;
    top: 175px;
    width: 27px;
    height: 27px;
  }
  .icon--phone { left: 131px; }
  .icon--mail  { left: 162px; }
  .icon--web   { left: 194px; }
  .contact-line {
    position: absolute;
    left: 0; width: 352px;
    margin: 0;
    font-size: 17px;
    color: var(--ink);
    letter-spacing: 0.5px;
  }
  .contact-line--phone { top: 219px; font-size: 18px; }
  .contact-line--email { top: 247px; font-size: 16px; }
  .contact-line--web   { top: 275px; font-size: 16px; }
  .address-line {
    position: absolute;
    left: 0; width: 352px;
    margin: 0;
    font-size: 17px;
    color: var(--ink);
    letter-spacing: 0.8px;
  }
  .address-line--street { top: 322px; }
  .address-line--city   { top: 349px; }

  .watermark-ring {
    position: absolute;
    left: 349px;
    top: 26px;
    width: 340px;
    height: 340px;
  }

  .brand-ring {
    position: absolute;
    left: 246px;
    top: 62px;
    width: 212px;
    height: 212px;
  }
  .brand-name {
    position: absolute;
    left: 0; width: 694px;
    top: 292px;
    margin: 0;
    text-align: center;
    font-size: 38px;
    font-weight: 600;
    letter-spacing: 0.5px;
    color: var(--navy);
  }
</style>
</head>
<body>
<div class="canvas">

  <section class="card card--front" aria-label="Business card front">
    <svg class="watermark-ring" viewBox="0 0 340 340" aria-hidden="true">
      <circle cx="170" cy="170" r="166" fill="none" stroke="var(--faint)" stroke-width="5"/>
    </svg>

    <div class="contact-column">
      <h1 class="company-heading">Brennick Holdings</h1>
      <h2 class="person-name">DANIEL HARTLEY</h2>
      <p class="person-title">Managing Director</p>

      <span class="rule rule--left"></span>
      <span class="rule rule--right"></span>

      <svg class="icon icon--phone" viewBox="0 0 27 27" aria-label="Phone">
        <rect width="27" height="27" rx="6" fill="var(--navy)"/>
        <path d="M7 11c0-2 3-3.5 6.5-3.5S20 9 20 11l-2.5 1-1-1.6h-6l-1 1.6z" fill="#fff"/>
        <rect x="8" y="13" width="11" height="7" rx="1.5" fill="#fff"/>
        <circle cx="13.5" cy="16.5" r="1.6" fill="var(--navy)"/>
      </svg>
      <svg class="icon icon--mail" viewBox="0 0 27 27" aria-label="Email">
        <rect width="27" height="27" rx="6" fill="var(--navy)"/>
        <rect x="6" y="8.5" width="15" height="10" rx="1.5" fill="#fff"/>
        <path d="M6.5 9.5l7 5 7-5" fill="none" stroke="var(--navy)" stroke-width="1.4"/>
      </svg>
      <svg class="icon icon--web" viewBox="0 0 27 27" aria-label="Website">
        <rect width="27" height="27" rx="6" fill="var(--navy)"/>
        <circle cx="13.5" cy="13.5" r="7" fill="#fff"/>
        <path d="M10 9.5c1.5 0 2 1.5 3.5 1.5s1 2-0.5 2.5-1 2.5-2.5 2.5-1.5-2-1-3.5zM15.5 15c1 0 2 .8 1.8 2.3-.4 1-1.6 1.3-2.1.2-.3-1 .3-2.5.3-2.5z" fill="var(--navy)"/>
      </svg>

      <p class="contact-line contact-line--phone">123 456 789</p>
      <p class="contact-line contact-line--email">INFO@YOUREMAIL.COM</p>
      <p class="contact-line contact-line--web">WWW.YOURWEBSITE.COM</p>

      <span class="rule rule--divider"></span>

      <p class="address-line address-line--street">Your address, City</p>
      <p class="address-line address-line--city">State, Zip 1234</p>
    </div>
  </section>

  <section class="card card--back" aria-label="Business card back">
    <svg class="brand-ring" viewBox="0 0 212 212" aria-hidden="true">
      <circle cx="106" cy="106" r="102" fill="none" stroke="var(--navy)" stroke-width="4"/>
    </svg>
    <p class="brand-name">Brennick Holdings</p>
  </section>

</div>
</body>
</html>
```